Your conflict - our mediation - joint conflict SOLUTION

With this flyer I am looking for conflict parties who are ready to tackle and resolve their conflict with a prospective mediator. The mediation is free because I am doing it as part of my diploma thesis. Time frame approx. 4 sessions of 2.5 hours each. The wishes and needs of both parties are listened to and “picked out”. In an open, constructive, appreciative framework, solutions are developed and negotiated together.

Target Market(s)

everyone who is ready to deal with himself and his counterpart and everyone who wants to work out a solution with the respect, openness and support of a mediator.

Requirements
Must have
• - "For my diploma thesis I am looking for conflicting parties who are willing to resolve their conflict with a mediator"
- Time frame: 4 x 2.5 hours feasible in Solothurn, Bern, Brugg
- Free of charge
- my coordinates - see business card
- more information at www.lindenhofwerk.ch
Nice to have
• the card should be based on the style of my homepage www.lindenhofwerk.ch and my business card

```html
<!DOCTYPE html>
<html lang="de">
<head>
<meta charset="utf-8">
<title>Mediation Flyer – Lindenhofwerk</title>
<link rel="stylesheet" href="https://fonts.googleapis.com/css2?family=Bebas+Neue&family=Lobster&family=Open+Sans:wght@400;600;700;800&display=swap">
<style>
  :root{
    --page-bg:#e4e5e7;
    --paper:#ffffff;
    --navy:#2b3a8f;
    --royal:#263a8c;
    --deep:#0e1858;
    --teal:#1b8088;
    --gold:#b99a6b;
    --green:#1a9a48;
    --white:#ffffff;
  }
  *{margin:0;padding:0;box-sizing:border-box}
  html,body{width:1200px;height:959px;overflow:hidden;background:var(--page-bg)}
  .flyer{
    position:absolute;left:240px;top:14px;width:719px;height:931px;
    background:var(--paper);overflow:hidden;
    box-shadow:0 4px 18px rgba(0,0,0,.18);
    font-family:"Open Sans",sans-serif;
  }
  .hero-photo{
    position:absolute;left:0;top:0;width:719px;height:570px;
    background:
      radial-gradient(ellipse 260px 200px at 470px 150px, rgba(255,255,255,.9), rgba(255,255,255,0) 70%),
      linear-gradient(180deg,#f4f5f5 0%,#dfe3e5 38%,#c6cfd3 60%,#b9c2c6 100%);
  }
  .hero-photo::after{
    content:"";position:absolute;left:300px;top:80px;width:360px;height:330px;
    background:radial-gradient(ellipse at 50% 55%, rgba(150,160,170,.55), rgba(150,160,170,0) 70%);
  }
  .brand-box{
    position:absolute;left:43px;top:0;width:238px;height:167px;
    background:var(--paper);
    clip-path:polygon(0 0,100% 0,100% 88%,50% 100%,0 88%);
    display:flex;align-items:center;justify-content:center;gap:10px;
  }
  .brand-dot{width:14px;height:14px;border-radius:50%;background:var(--gold)}
  .brand-name{font-weight:600;font-size:24px;color:var(--navy);letter-spacing:.3px}
  .headline{
    position:absolute;left:50px;top:194px;
    font-family:"Bebas Neue",sans-serif;font-weight:400;font-size:31px;line-height:28px;color:var(--navy);
  }
  .timeframe{position:absolute;left:50px;top:282px;color:var(--navy)}
  .timeframe-title{font-weight:700;font-size:17px;line-height:22px}
  .timeframe-text{font-size:16px;line-height:22px;margin-top:2px}
  .waves{position:absolute;left:0;top:0}
  .topics{
    position:absolute;left:42px;top:425px;display:flex;gap:20px;
    color:var(--white);font-size:27px;letter-spacing:-.3px;
  }
  .topic{display:flex;align-items:center;gap:5px}
  .topic svg{flex:none}
  .badge{position:absolute;left:536px;top:352px;width:170px;height:170px}
  .badge-text{
    position:absolute;left:0;top:0;width:170px;height:170px;
    display:flex;flex-direction:column;align-items:center;justify-content:center;
    color:var(--white);font-weight:700;line-height:1;
  }
  .badge-text .big{font-size:30px}
  .badge-text .of{font-family:"Lobster",cursive;font-size:26px;font-weight:400;margin:1px 0}
  .body-copy{position:absolute;left:0;width:719px;text-align:center;color:var(--white)}
  .lead{top:539px;font-weight:700;font-size:13px;letter-spacing:-.5px;left:40px;width:660px}
  .relations{top:568px;font-size:13.5px;line-height:23.5px;letter-spacing:-.25px;padding:0 28px 0 40px}
  .question{top:666px;font-weight:600;font-size:25px}
  .thesis{top:704px;font-family:"Lobster",cursive;font-size:22px;line-height:30px;padding:0 40px 0 55px}
  .mediator{top:782px;font-weight:700;font-size:27px;color:var(--green)}
  .contacts{
    position:absolute;left:44px;top:880px;right:20px;display:flex;
    color:var(--navy);font-size:16px;line-height:20px;
  }
  .contact{display:flex;align-items:center;gap:8px}
  .contact:nth-child(1){width:261px}
  .contact:nth-child(2){width:214px}
</style>
</head>
<body>
<main class="flyer">
  <div class="hero-photo" role="img" aria-label="Photo: a couple sitting back to back in meditation on a wooden jetty by a misty mountain lake"></div>

  <div class="brand-box">
    <span class="brand-dot"></span>
    <span class="brand-name">Lindenhofwerk</span>
  </div>

  <h1 class="headline">Ihr Konflikt<br>Unsere Mediation<br>Gemeinsame Konfliktlösung</h1>

  <div class="timeframe">
    <p class="timeframe-title">ČASOVÝ RÁMEC:</p>
    <p class="timeframe-text">4 x 2,5 hodiny proveditelné v<br>Solothurn, Bern, Brugg</p>
  </div>

  <svg class="waves" width="719" height="931" viewBox="0 0 719 931">
    <defs>
      <linearGradient id="bodyGrad" x1="0" y1="0" x2="0" y2="1">
        <stop offset="0" stop-color="#1b8088"/>
        <stop offset="0.22" stop-color="#22408e"/>
        <stop offset="0.6" stop-color="#1a2a78"/>
        <stop offset="1" stop-color="#0e1858"/>
      </linearGradient>
    </defs>
    <path d="M0,400 C150,370 350,368 480,405 C560,428 660,478 719,520 L719,931 L0,931 Z" fill="url(#bodyGrad)"/>
    <path d="M0,400 C150,370 350,368 480,405 C560,428 660,478 719,520 L719,545 C600,505 450,488 300,498 C180,506 80,505 0,492 Z" fill="var(--royal)"/>
    <path d="M0,395 C150,365 350,363 480,400 C560,423 660,473 719,515" fill="none" stroke="#ffffff" stroke-width="5" opacity=".85"/>
    <path d="M0,814 C220,860 480,872 719,806" fill="none" stroke="#c9ccd2" stroke-width="6"/>
    <path d="M0,818 C220,864 480,876 719,810 L719,931 L0,931 Z" fill="var(--paper)"/>
  </svg>

  <div class="topics">
    <span class="topic"><svg width="18" height="18" viewBox="0 0 18 18"><circle cx="9" cy="9" r="8.5" fill="#fff"/><path d="M5 9.3l2.6 2.5L13 6.5" fill="none" stroke="#263a8c" stroke-width="2"/></svg>KONFLIKT</span>
    <span class="topic"><svg width="18" height="18" viewBox="0 0 18 18"><circle cx="9" cy="9" r="8.5" fill="#fff"/><path d="M5 9.3l2.6 2.5L13 6.5" fill="none" stroke="#263a8c" stroke-width="2"/></svg>STREIT</span>
    <span class="topic"><svg width="18" height="18" viewBox="0 0 18 18"><circle cx="9" cy="9" r="8.5" fill="#fff"/><path d="M5 9.3l2.6 2.5L13 6.5" fill="none" stroke="#263a8c" stroke-width="2"/></svg>&nbsp;BLOCKADE</span>
  </div>

  <div class="badge">
    <svg width="170" height="170" viewBox="0 0 170 170">
      <g fill="var(--gold)" transform="translate(85 85)">
        <rect x="-62" y="-62" width="124" height="124" rx="6"/>
        <rect x="-62" y="-62" width="124" height="124" rx="6" transform="rotate(22.5)"/>
        <rect x="-62" y="-62" width="124" height="124" rx="6" transform="rotate(45)"/>
        <rect x="-62" y="-62" width="124" height="124" rx="6" transform="rotate(67.5)"/>
      </g>
    </svg>
    <div class="badge-text"><span class="big">FREE</span><span class="of">of</span><span class="big">CHARGE</span></div>
  </div>

  <p class="body-copy lead">MEDIATION - GEMEINSAM LÖSUNGEN SUCHEN UND FINDEN, DIE ALLE PARTEIEN MITTRAGEN KÖNNEN</p>
  <p class="body-copy relations">mit Ihrer Ehefrau … Ihrem Vertragspartner … Ihrer Nachbarin … Ihrem Mieter … Ihrer Tochter … Ihrem Pächter … Ihrer Schwester … Ihrem Geschäftspartner … Ihrer Vorgesetzten … Ihrem Mitarbeiter … Ihrem Vater … Ihrer Vermieterin … Ihrem Freund …</p>
  <p class="body-copy question">Sie kommen nicht mehr weiter?</p>
  <p class="body-copy thesis">Ve své diplomové práci hledám konfliktní strany, které jsou ochotny vyřešit jejich konflikt s prostředníkem</p>
  <p class="body-copy mediator">Sabine Keller Arnold</p>

  <footer class="contacts">
    <span class="contact"><svg width="14" height="14" viewBox="0 0 14 14"><circle cx="7" cy="7" r="7" fill="var(--green)"/><g fill="none" stroke="#fff" stroke-width="1"><circle cx="7" cy="7" r="4"/><ellipse cx="7" cy="7" rx="1.8" ry="4"/><path d="M3 7h8"/></g></svg>www.lindenhofwerk.ch</span>
    <span class="contact"><svg width="14" height="14" viewBox="0 0 14 14"><circle cx="7" cy="7" r="7" fill="var(--green)"/><path d="M4.3 3.8c.4-.4.9-.4 1.1 0l.8 1.3c.2.3.1.7-.2.9l-.4.3c.4 1 1.1 1.7 2.1 2.1l.3-.4c.2-.3.6-.4.9-.2l1.3.8c.4.2.4.7 0 1.1-.7.7-1.8.9-2.8.3-1.6-.9-2.8-2.1-3.6-3.6-.5-1-.3-2 .5-2.6z" fill="#fff"/></svg>078 555 41 27</span>
    <span class="contact"><svg width="14" height="14" viewBox="0 0 14 14"><circle cx="7" cy="7" r="7" fill="var(--green)"/><rect x="3.5" y="4.5" width="7" height="5" fill="none" stroke="#fff" stroke-width="1"/><path d="M3.5 4.5L7 7.3l3.5-2.8" fill="none" stroke="#fff" stroke-width="1"/></svg>s.keller@mailbox.ch</span>
  </footer>
</main>
</body>
</html>
```